Postcard and Door Hanger Design

We need two pieces designed for marketing. Both will use the same logo and photo just the text will be slightly different. We need these designs looking very modern, clean, and simple while having the important information to stand out.

Postcard: 2 sided
- Side 1 just have large logo with our website and phone number
- Side 2 below.
- 4 x 6
- Use photo of house provided
- "Going Above and Beyond Every Time"
- "Call TODAY to Reserve your project by May 1st and receive 10% off"
- "Residential and Commercial"
- Our contact is 778-294-1175
- Website is www.velmarcoatings.com
- Might include something like "check out our portfolio on our website"

Use the above as a guidline and be creative with it, add or take away as you see fit as we are open to suggestions.

Door Hanger: 2 sided
Side 1 - Logo with contact details
Side 2 - Below
- 4 x 11
- "We are painting your neighborhood"
-"come see us in action at (then leave a space where we can stick a label onto our door hanger with an address of a home we are painting)
- Call today for a FREE ESTIMATE
- 778-294-1175
- www.velmarcoatings.com

Links:

https://www.filenook.net/sh/q3k8tz52rwa9pn/TR7XKLP-QZ

https://www.filenook.net/sh/xv6rr27jtl3wyd/HNwLRaPqTs

Logo File:

https://www.filenook.net/sh/p2d94hzb1wkq07/zfa-R9LKiv

```html
<!DOCTYPE html>
<html lang="en">
<head>
<meta charset="utf-8">
<title>Velmar Coatings Door Hanger</title>
<link rel="stylesheet" href="https://fonts.googleapis.com/css2?family=Josefin+Sans:wght@300;400&family=Libre+Baskerville:wght@400;700&family=Stardos+Stencil:wght@700&display=swap">
<style>
  :root {
    --slate: #45535e;
    --teal: #17bcb8;
    --band-grey: #a9aeb2;
    --wall-light: #ecebea;
    --wall-shade: #d9d8d6;
    --paper: #ffffff;
    --label-bg: #444444;
    --ink-light: #ffffff;
  }
  * { margin: 0; padding: 0; box-sizing: border-box; }
  html, body { width: 1200px; height: 848px; overflow: hidden; background: var(--paper); }
  .canvas { position: relative; width: 1200px; height: 848px; }

  .sheet-title {
    position: absolute; left: 877px; top: 40px; width: 303px; height: 47px;
    background: var(--label-bg); color: var(--ink-light);
    font: 400 21px/47px "Libre Baskerville", serif; text-align: center;
  }

  .hanger { position: absolute; top: 22px; width: 295px; height: 810px; overflow: hidden; }
  .hanger--front { left: 137px; }
  .hanger--back { left: 515px; }
  .hanger__shape { position: absolute; inset: 0; }

  .phone-icon { display: inline-block; vertical-align: middle; fill: var(--ink-light); }

  /* Front side */
  .brand {
    position: absolute; left: 0; width: 100%; top: 340px; text-align: center; color: var(--ink-light);
  }
  .brand__mark { display: block; width: 26px; height: 26px; margin: 0 auto 44px; background: var(--teal); }
  .brand__name { font: 300 24px/1 "Josefin Sans", sans-serif; letter-spacing: 2px; white-space: nowrap; }
  .web-band {
    position: absolute; left: 0; width: 100%; top: 476px; height: 36px;
    background: var(--band-grey); color: var(--slate);
    font: 400 13px/36px "Libre Baskerville", serif; letter-spacing: 1.5px; text-align: center;
  }
  .front-phone {
    position: absolute; left: 0; width: 100%; top: 522px; text-align: center;
    color: var(--ink-light); font: 700 17px/22px "Libre Baskerville", serif; letter-spacing: 1px;
  }

  /* Back side */
  .estimate { position: absolute; left: 0; width: 100%; top: 258px; text-align: center; color: var(--ink-light); }
  .estimate__phone { font: 700 25px/34px "Libre Baskerville", serif; letter-spacing: 1px; }
  .estimate__note { font: 700 12px/16px "Libre Baskerville", serif; letter-spacing: 0.5px; }

  .wall {
    position: absolute; left: 0; top: 324px; width: 100%; height: 419px;
    background: radial-gradient(ellipse at 40% 40%, var(--wall-light), var(--wall-shade));
  }
  .brush-photo {
    position: absolute; left: 158px; top: 138px; width: 137px; height: 72px;
    background: linear-gradient(120deg, #d8c3a0 0%, #e8cbb4 45%, #a3262a 75%, #e2c1a8 100%);
    opacity: 0.55; border-radius: 36px 0 0 36px;
  }
  .headline {
    position: absolute; left: 22px; top: 26px; width: 260px; color: var(--slate);
    font: 700 37px/61px "Stardos Stencil", sans-serif; letter-spacing: 3px; white-space: nowrap;
  }
  .headline__small { font-size: 26px; letter-spacing: 1px; margin-left: -10px; }
  .action-band {
    position: absolute; left: 0; top: 276px; width: 100%; height: 19px;
    background: var(--slate); color: var(--ink-light);
    font: 700 12px/19px "Libre Baskerville", serif; letter-spacing: 1px; text-align: center;
  }
  .action-arrow { position: absolute; left: 127px; top: 295px; }
  .address-space { position: absolute; left: 0; top: 320px; width: 100%; height: 90px; }

  .back-web {
    position: absolute; left: 0; top: 743px; width: 100%; height: 27px;
    background: var(--slate); color: var(--ink-light);
    font: 700 11px/27px "Libre Baskerville", serif; letter-spacing: 1px; text-align: center;
  }
</style>
</head>
<body>
<main class="canvas">
  <div class="sheet-title">VELMAR Door Hanger</div>

  <section class="hanger hanger--front">
    <svg class="hanger__shape" width="295" height="810" viewBox="0 0 295 810">
      <path fill="var(--slate)" fill-rule="evenodd"
        d="M0,148 A147.5,147.5 0 0 1 295,148 V770 H0 Z M146,57 a97,97 0 1 0 0.01,0 Z"/>
      <rect x="0" y="770" width="295" height="40" fill="var(--teal)"/>
      <line x1="242" y1="156" x2="295" y2="156" stroke="var(--paper)" stroke-width="3"/>
    </svg>
    <div class="brand">
      <span class="brand__mark"></span>
      <div class="brand__name">VELMAR COATINGS</div>
    </div>
    <div class="web-band">WWW.VELMARCOATINGS.COM</div>
    <div class="front-phone">
      <svg class="phone-icon" width="18" height="14" viewBox="0 0 24 18"><path d="M2,6 C2,1 22,1 22,6 L18,8 L16,5 H8 L6,8 Z M5,9 H19 L21,17 H3 Z"/></svg>
      778-294-1175
    </div>
  </section>

  <section class="hanger hanger--back">
    <svg class="hanger__shape" width="295" height="810" viewBox="0 0 295 810">
      <path fill="var(--slate)" fill-rule="evenodd"
        d="M0,148 A147.5,147.5 0 0 1 295,148 V770 H0 Z M146,57 a97,97 0 1 0 0.01,0 Z"/>
      <rect x="0" y="770" width="295" height="40" fill="var(--teal)"/>
      <line x1="242" y1="156" x2="295" y2="156" stroke="var(--paper)" stroke-width="3"/>
    </svg>
    <div class="estimate">
      <div class="estimate__phone">
        <svg class="phone-icon" width="36" height="26" viewBox="0 0 24 18"><path d="M2,6 C2,1 22,1 22,6 L18,8 L16,5 H8 L6,8 Z M5,9 H19 L21,17 H3 Z"/></svg>
        778-294-1175
      </div>
      <div class="estimate__note">Call for a FREE ESTIMATE quote</div>
    </div>
    <div class="wall" role="img" aria-label="Photo of a white textured wall">
      <div class="brush-photo" role="img" aria-label="Photo of a hand holding a paint brush"></div>
      <h1 class="headline">WE ARE<br>PAINTING<br>YOUR<br><span class="headline__small">NEIGHBORHOOD</span></h1>
      <div class="action-band">COME SEE US IN ACTION AT</div>
      <svg class="action-arrow" width="40" height="20" viewBox="0 0 40 20"><path d="M0,0 H40 L20,20 Z" fill="var(--slate)"/></svg>
      <div class="address-space" aria-label="Space for address label"></div>
    </div>
    <div class="back-web">WWW.VELMARCOATINGS.COM</div>
  </section>
</main>
</body>
</html>
```